2 sided flyer for Insurance Servics

Would like a flyer that talks about who we are, our services, and our process. Attaching relevant information, as well as our Logo and other logos for a few larger insurance carriers that we have access to.

Target Market(s)

Financial Advisors and Insurance Agents

Industry/Entity Type

Finance and Insurance

Colors
0054AA
0677BA
7BADD7
CADEEF
E8F1F8
F0912C
F2A743
F7CA91
FBE8D2
FDF5EE

Requirements
Must have
• Lists, bullet points, pictures, and logos uploaded

```html
<!DOCTYPE html>
<html lang="en">
<head>
<meta charset="utf-8">
<title>Harborline Risk Partners – Two-Sided Flyer</title>
<link href="https://fonts.googleapis.com/css2?family=Carlito:ital,wght@0,400;0,700;1,400;1,700&family=Oswald:wght@300;400&display=swap" rel="stylesheet">
<style>
  :root{
    --blue-deep:#0054AA;
    --blue:#0677BA;
    --blue-soft:#7BADD7;
    --blue-pale:#CADEEF;
    --blue-mist:#E8F1F8;
    --orange:#F0912C;
    --orange-warm:#F2A743;
    --orange-soft:#F7CA91;
    --peach:#FBE8D2;
    --cream:#FDF5EE;
    --ink:#3a3a3a;
    --stage:#ebebeb;
  }
  *{box-sizing:border-box;margin:0;padding:0}
  html,body{width:1200px;height:840px;overflow:hidden}
  body{background:var(--stage);font-family:"Carlito",Calibri,sans-serif;color:var(--ink);position:relative}

  .page{position:absolute;top:30px;width:570px;height:780px;background:#fff;box-shadow:0 6px 22px rgba(0,0,0,.18);overflow:hidden}
  .page--front{left:20px}
  .page--back{left:610px}

  p{font-size:9.6px;line-height:1.22}
  .tab{display:inline-block;background:var(--orange);color:#fff;font-weight:700;font-size:11px;padding:2px 26px 2px 8px;clip-path:polygon(0 0,100% 0,calc(100% - 8px) 100%,0 100%)}
  .tab--blue{background:var(--blue-deep)}
  .tab--italic{font-style:italic;font-size:12px}
  .rule-head{color:var(--blue-deep);font-weight:700;font-style:italic;font-size:11.5px;border-bottom:1.5px solid var(--blue);padding-bottom:1px;margin-bottom:3px}
  .bullet-head{color:var(--orange);font-weight:700;font-style:italic;font-size:11.5px;border-bottom:1.5px solid var(--orange);margin-bottom:2px;padding-left:12px;position:relative}
  .bullet-head::before{content:"";position:absolute;left:1px;top:5px;width:5px;height:5px;border-radius:50%;background:var(--orange)}

  /* front header */
  .brand{position:absolute;left:18px;top:16px;display:flex;align-items:center;gap:8px}
  .brand__mark{width:34px;height:34px;background:var(--blue-pale)}
  .brand__name{font-weight:700;font-size:11px;line-height:1.05;color:var(--blue-deep);text-transform:uppercase}
  .tagline{position:absolute;left:200px;top:22px;width:200px;background:var(--orange);color:#fff;font-family:"Oswald",sans-serif;font-weight:300;font-size:11px;line-height:1.15;padding:4px 8px;text-align:right}
  .about{position:absolute;left:0;top:62px;width:380px}
  .about__body{background:var(--blue-deep);color:#fff;padding:6px 12px 9px 16px;border-bottom:3px solid var(--orange)}
  .about__body p{font-size:9.6px;text-align:justify}
  .hero-photo{position:absolute;left:392px;top:54px;width:160px;height:192px;border:5px solid var(--blue);border-radius:0 70px 0 70px;background:linear-gradient(180deg,#2d6fb8 0%,#9cc3e6 45%,#d7e6c2 70%,#6f8a3e 100%)}

  .why{position:absolute;left:0;top:204px;width:380px;height:48px}
  .why .tab{position:absolute;left:0;top:8px}
  .slogan{position:absolute;left:108px;top:0;width:270px;height:48px;font-family:"Oswald",sans-serif;font-weight:300;color:var(--orange);font-size:10px;line-height:1.1}
  .slogan span{position:absolute;white-space:nowrap}
  .slogan__lead{left:0;top:2px}
  .slogan__name{left:72px;top:4px;font-weight:400;font-size:26px;line-height:1}
  .slogan__value{left:124px;top:12px}
  .slogan__close{left:134px;top:30px;font-size:12px}

  .why-grid{position:absolute;left:16px;top:258px;width:540px;display:grid;grid-template-columns:1fr 1fr;gap:10px}
  .why-card{background:var(--cream);border-radius:10px;padding:8px 10px}
  .why-card p{margin-bottom:6px;text-align:justify}

  .services{position:absolute;left:0;top:474px;width:570px}
  .services .tab{float:left;margin:0 8px 0 0}
  .services p{padding:2px 16px 0 0}

  .pos{position:absolute;left:0;top:536px;width:570px}
  .pos__intro{padding:3px 16px 0 16px}
  .pos__grid{display:grid;grid-template-columns:1fr 1fr 1fr;gap:10px;padding:8px 16px 0}
  .pos__grid p{text-align:justify}
  .quote{background:var(--orange);color:#fff;font-style:italic;font-size:10px;line-height:1.2;padding:6px 10px;border-radius:10px;position:relative}
  .quote::after{content:"";position:absolute;left:18px;bottom:-7px;border:7px solid transparent;border-top-color:var(--orange);border-bottom:0}
  .quote-by{color:var(--orange);font-weight:700;font-size:11px;margin-top:9px}
  .quote-by span{color:var(--ink);font-weight:400;font-style:italic;font-size:9.6px}
  .quote-wrap{position:absolute;right:16px;top:0;width:200px}

  .concierge{position:absolute;left:0;top:706px;width:570px}
  .concierge p{padding:3px 16px 0 16px}

  /* back */
  .back-top{position:absolute;left:12px;top:14px;width:546px;display:grid;grid-template-columns:1fr 1fr;gap:14px}
  .back-col{background:var(--cream);border-radius:10px;padding:10px}
  .back-col p{margin-bottom:6px;text-align:justify}
  .back-col .quote{margin:4px 0 0}
  .back-col .quote-by{margin-bottom:8px}

  .process{position:absolute;left:12px;top:420px;width:546px;background:var(--blue-deep);color:#fff;border-radius:14px;padding:8px 14px 12px}
  .process .tab{margin:-2px 0 6px -14px}
  .process__grid{display:grid;grid-template-columns:1fr 1fr;gap:6px 18px}
  .step h4{font-size:11.5px;font-weight:700;font-style:italic;border-bottom:1.5px solid #fff;margin-bottom:2px}
  .step ol{list-style:lower-alpha;padding-left:14px;font-size:9.6px;line-height:1.22}

  .closing{position:absolute;left:14px;top:640px;width:250px}
  .closing p{font-size:9px;margin-bottom:6px}
  .email{display:inline-block;background:var(--orange);color:#fff;font-weight:700;font-size:9.6px;padding:2px 10px}
  .carriers{position:absolute;left:286px;top:640px;width:270px}
  .carriers .tab{margin-bottom:8px}
  .carrier-grid{display:grid;grid-template-columns:repeat(6,1fr);gap:8px 6px}
  .carrier-badge{height:22px;border-radius:3px;background:var(--blue-pale)}
  .carrier-badge--deep{background:var(--blue-deep)}
  .carrier-badge--round{border-radius:50%;width:22px;justify-self:center;background:var(--blue-soft)}
  .carrier-badge--warm{background:var(--orange-soft)}
</style>
</head>
<body>

<section class="page page--front">
  <div class="brand">
    <div class="brand__mark"></div>
    <div class="brand__name">Harborline<br>Risk<br>Partners</div>
  </div>
  <div class="tagline">WE LOOK FORWARD TO USING OUR EXPERTISE TO HELP YOU GROW YOUR BUSINESS.</div>

  <div class="about">
    <span class="tab">About Us</span>
    <div class="about__body">
      <p>Harborline Risk Partners is a full-service life insurance Brokerage General Agency (BGA) and serves financial advisors, independent insurance agents, and banks throughout the United States. Having served our customers for over 25 years, we are committed to helping financial advisors achieve their goals for their clients. Serving as a one-stop shop for all life insurance solutions, we offer a wide range of insurance products from multiple carriers, giving our advisors and agents access to a variety of options and solutions to meet their clients’ needs.</p>
    </div>
  </div>

  <div class="hero-photo" role="img" aria-label="Photo of a golfer mid-swing on a green course under a blue sky"></div>

  <div class="why">
    <span class="tab tab--blue">Why HRP?</span>
    <div class="slogan">
      <span class="slogan__lead">WHEN YOU CHOSE<br>TO WORK WITH</span>
      <span class="slogan__name">HRP,</span>
      <span class="slogan__value">YOU WILL ADD VALUE</span>
      <span class="slogan__close">TO YOUR FIRM …OVERNIGHT!</span>
    </div>
  </div>

  <div class="why-grid">
    <div class="why-card">
      <h3 class="rule-head">1. Immediate Risk Management Partner</h3>
      <p>We know insurance and understand your business. Your agents will have access to a wide range of carriers, giving them options to meet client needs. In addition, we only deal in insurance…so rest assured we leave the money management to you!</p>
      <h3 class="rule-head">2. Experienced Insurance Specialists</h3>
      <p>Our Point of Sales Specialists have many years of industry experience, hold various designations, and are licensed to provide a variety of products. These trained professionals are located throughout the country and are ready to provide prompt service to your staff.</p>
    </div>
    <div class="why-card">
      <h3 class="rule-head">3. Customized Concierge Service</h3>
      <p>This team of professionals leverage their experience and technology to remove the pain points of writing policies. Comprised of our licensing, application, and case management specialists, we handle every spect of the process. No more application paperwork or underwriting hassle for your staff!</p>
      <h3 class="rule-head">4. Save Time and Money</h3>
      <p>We have designed our services to operate efficiently, funded from the compensation we receive by the insurance carriers, meaning no cost to you. Our goal is to increase your production, while eliminating your internal salaries and benefits dedicated to insurance support.</p>
    </div>
  </div>

  <div class="services">
    <span class="tab tab--italic">Our Services</span>
    <p>As a BGA, our mission is to connect agents and advisors with insurance carriers and help our customers find the correct product that meets each client’s needs. From our experienced Point of Sale Strategists to our professional Concierge Service Team, we provide value every step of the way, at no additional cost!</p>
  </div>

  <div class="pos">
    <span class="tab tab--italic">Our Point of Sale Strategists</span>
    <p class="pos__intro" style="width:360px">Work directly with agents and advisors to provide experienced assistance for immediate client needs, as well as maximizing insurance planning to find opportunities for all clients.</p>
    <div class="quote-wrap">
      <div class="quote">“From quote to issue and review to service, each case is an opportunity of quality care.”</div>
      <div class="quote-by">Dana R, <span>New Business Specialist</span></div>
    </div>
    <div class="pos__grid">
      <div>
        <h4 class="bullet-head">Dedicated Strategists</h4>
        <p>We develop a personal relationship with each advisor, giving you confidence that we are working in your best interest. Always here to help with quotes and analysis.</p>
      </div>
      <div>
        <h4 class="bullet-head">Quotes Made Easy</h4>
        <p>Access our online system or simply email your specialist to receive quotes for your client reviews, life event circumstances, estate needs, or prospect meetings.</p>
      </div>
      <div>
        <h4 class="bullet-head">National Footprint</h4>
        <p>Our team is nationwide, allowing us to serve you regardless of location, time zone, or licensing limitations.</p>
      </div>
    </div>
  </div>

  <div class="concierge">
    <span class="tab tab--italic">Our Concierge Service Team</span>
    <p>is comprised of several specialists. Once an agent moves forward with an application, simply hand it off to our staff, ensuring your policy is processed accurately and delivered in a timely manner.</p>
  </div>
</section>

<section class="page page--back">
  <div class="back-top">
    <div class="back-col">
      <div class="quote">“My go-to person for anything the agent needs, handling everything from A to Z!”</div>
      <div class="quote-by">Jamie L, <span>Application Specialist/Case Manager</span></div>
      <h4 class="bullet-head">Clarity</h4>
      <p>Experience allows us to provide correct quotes as well as properly relay carrier processes and manage expectations.</p>
      <h4 class="bullet-head">Network</h4>
      <p>Our reach is nationwide, allowing us to serve you regardless of time zone, or licensing limitations.</p>
      <div class="quote">“Clients are never uncomfortable sharing their history to their advisor with someone in our office, who have their best interest.”</div>
      <div class="quote-by">Riley P, <span>Application Specialist</span></div>
      <h4 class="bullet-head">Application Specialists</h4>
      <p>We provide correct forms and properly relay carrier expectations.</p>
      <p>We order medical records and exams for clients, speeding the process by days if needed.</p>
      <p>We utilize electronic signatures for agent and client, where possible.</p>
    </div>
    <div class="back-col">
      <h4 class="bullet-head">Dedicated Case Managers</h4>
      <p>Your personal case manager gives us a better understanding of your business, expectations, and preferred process.</p>
      <h4 class="bullet-head">Agent Licensing</h4>
      <p>Access our online system or simply email your specialist to receive quotes for your client reviews, life event circumstances, estate needs, or prospect meetings.</p>
      <h4 class="bullet-head">No Fluff Process</h4>
      <p>We create a seamless process by gathering what is required for underwriting, eliminating the unnecessary back and forth with clients that often delays the policy and annoys clients.</p>
      <div class="quote">“Our weekly updates keep advisors well informed throughout the process.”</div>
      <div class="quote-by">Morgan T, <span>Senior Case Manager</span></div>
      <h4 class="bullet-head">Recurring Updates</h4>
      <p>Your case manager will keep you updated on the status of all cases.</p>
      <h4 class="bullet-head">Online Case Tracker</h4>
      <p>This tool allows you to access the status of your cases. All carriers. All cases. All the time.</p>
      <h4 class="bullet-head">Policy Delivery</h4>
      <p>We ensure premiums are paid and policy documents are delivered.</p>
    </div>
  </div>

  <div class="process">
    <span class="tab tab--italic">Our Process</span>
    <div class="process__grid">
      <div class="step">
        <h4>1. Quotes &amp; Analysis</h4>
        <ol><li>Access to multiple carriers, including most industry leaders.</li><li>Submit quotes online or simply email our staff.</li><li>Consult our Specialists to find the best solution for your client.</li></ol>
      </div>
      <div class="step">
        <h4>2. Contracting</h4>
        <ol><li>Whether to get appointed is up to you; we guide each step.</li><li>Electronic signatures make the appointment process fast and easy.</li></ol>
      </div>
      <div class="step">
        <h4>3. Applications &amp; Underwriting</h4>
        <ol><li>Our specialists oversee the entire application and underwriting process.</li><li>Direct contact with the client, ensuring confidential and private medical history conversation.</li><li>Utilize technology to provide electronic signatures where possible.</li></ol>
      </div>
      <div class="step">
        <h4>4. Policy Delivery &amp; Payout</h4>
        <ol><li>Ensure policy documents are delivered in full and on time.</li><li>Confirm premiums are paid and policies are in force.</li><li>Facilitate payout for all of your policies.</li></ol>
      </div>
    </div>
  </div>

  <div class="closing">
    <p>At HRP, we are dedicated to developing lasting relationships with all our of our customers, both current and new. If you have any insurance questions or would like to know how best to work with HRP, please contact us today.</p>
    <span class="email">contact@harborline-risk.com</span>
  </div>

  <div class="carriers">
    <span class="tab tab--italic">List of Carriers include</span>
    <div class="carrier-grid">
      <div class="carrier-badge carrier-badge--deep"></div>
      <div class="carrier-badge carrier-badge--deep"></div>
      <div class="carrier-badge"></div>
      <div class="carrier-badge carrier-badge--warm"></div>
      <div class="carrier-badge"></div>
      <div class="carrier-badge carrier-badge--deep"></div>
      <div class="carrier-badge"></div>
      <div class="carrier-badge carrier-badge--deep"></div>
      <div class="carrier-badge"></div>
      <div class="carrier-badge carrier-badge--round"></div>
      <div class="carrier-badge"></div>
      <div class="carrier-badge carrier-badge--round"></div>
    </div>
  </div>
</section>

</body>
</html>
```